A simple Chatterbook Ad (not Chatterbook Page) for weight loss surgery

It’s a simple ad in terms of the text.

The text should say:
Curious about weight loss surgery?
This 30 second quiz will tell you which procedure will suit you best

I'm open to variations in the text if it is thought to enhance the ad.

Targeted towards obese individuals who have been unable to lose weight with diet and exercise. My industry is weight loss surgery – webpage www.marcusbellweather.com.au. Clicking the ad leads to a quiz on my webpage relating to weight loss surgery. Most frequent users of this service are females (75%) between ages of 35 and 55 years.

Successful weight loss surgery can enable individuals who have been unable to lose weight to lose a substantial amount of the excess weight they are carrying to be healthier and happier.

```html
<!DOCTYPE html>
<html lang="en">
<head>
<meta charset="utf-8">
<title>Weight Loss Surgery Quiz Ad</title>
<link rel="stylesheet" href="https://fonts.googleapis.com/css2?family=Arimo:wght@400;700&display=swap">
<style>
  :root {
    --paper: #ffffff;
    --sky: #b9d1f2;
    --sky-soft: #d6e4f7;
    --scale-blue: #3b6fa8;
    --ink: #464646;
    --ink-body: #333333;
    --accent-text: #4a7aa0;
    --cta: #ff2a4c;
    --cta-text: #ffffff;
  }
  html, body {
    margin: 0;
    padding: 0;
    overflow: hidden;
    background: var(--paper);
  }
  .ad {
    position: relative;
    width: 1200px;
    height: 1200px;
    overflow: hidden;
    background: var(--paper);
    font-family: "Arimo", Arial, sans-serif;
  }
  .ad__backdrop {
    position: absolute;
    inset: 0;
  }
  .ad__dots {
    position: absolute;
    left: 48px;
    top: 52px;
    width: 88px;
    height: 32px;
    background: var(--sky);
    border-radius: 6px;
    opacity: 0.8;
  }
  .ad__illustration {
    position: absolute;
    left: 272px;
    top: 44px;
    width: 670px;
    height: 540px;
    border-radius: 40px 40px 60px 60px;
    background: radial-gradient(ellipse at 50% 55%, var(--scale-blue) 0%, #6f97c9 38%, var(--sky) 68%, var(--sky-soft) 100%);
  }
  .ad__headline {
    position: absolute;
    left: 0;
    right: 0;
    top: 622px;
    margin: 0;
    text-align: center;
    font-weight: 400;
    font-size: 58px;
    line-height: 68px;
    color: var(--ink);
  }
  .ad__headline-accent {
    color: var(--accent-text);
  }
  .ad__subline {
    position: absolute;
    left: 0;
    right: 0;
    top: 776px;
    margin: 0;
    text-align: center;
    font-weight: 400;
    font-size: 42px;
    line-height: 52px;
    color: var(--ink-body);
  }
  .ad__cta {
    position: absolute;
    left: 431px;
    top: 980px;
    width: 358px;
    height: 94px;
    border-radius: 10px;
    background: var(--cta);
    color: var(--cta-text);
    font-weight: 700;
    font-size: 33px;
    display: flex;
    align-items: center;
    justify-content: center;
  }
</style>
</head>
<body>
  <main class="ad">
    <svg class="ad__backdrop" width="1200" height="1200" viewBox="0 0 1200 1200" aria-hidden="true">
      <path d="M0,711 Q600,1310 1200,733 L1200,1200 L0,1200 Z" fill="var(--sky)"/>
    </svg>

    <div class="ad__dots" role="img" aria-label="Small grid of light blue decorative dots"></div>

    <div class="ad__illustration" role="img"
         aria-label="Illustration of a doctor with a clipboard beside a woman standing on a scale, in front of a large weighing dial with heart, blood drop and stomach icons"></div>

    <h1 class="ad__headline">
      Curious about<br>
      <span class="ad__headline-accent">weight loss</span> surgery?
    </h1>

    <p class="ad__subline">
      This 30 second quiz will tell<br>
      you which procedure will<br>
      suit you best
    </p>

    <div class="ad__cta">Get Started</div>
  </main>
</body>
</html>
```